Aviation club power point template

Hello designers
we are a small aviation club with about 100 members in germany. we love flying and are looking for a professional power point template for our public relations.
Here is the link to our homepage
https://www.lgk-treblingen.de/
the template should be aviation related and should be about gliders and small powered aircraft.
Here you can find our gliders (you see the right link only in german language)
https://www.lgk-treblingen.de/flying/gliding/
Here you can find our motor planes (Only Falke KX-250) (you see the right link only in German language)
https://www.lgk-treblingen.de/flying/motorflying/
I found a model of the Falke KX-250 motor plane, but in green. We have a red-white painting
http://www.planzumodel.com/wp-content/uploads/Image10-300x198. png
Required foils:
3 welcome (one neutral, one glider, one powered plane)
1-2 agenda
2-3 statistics
2-3 enumerations
2-3 free slides
We look forward to your suggestions and thank you in advance for your work. If you have any questions or need more data. Please write us.
greetings
jorg

```html
<!DOCTYPE html>
<html lang="de">
<head>
<meta charset="utf-8">
<title>Luftsportklub Treblingen – Präsentationsvorlage</title>
<link href="https://fonts.googleapis.com/css2?family=Montserrat:wght@400;500;600;700;800&display=swap" rel="stylesheet">
<style>
  :root{
    --board:#efeff0;
    --shadow:#d1d2d4;
    --white:#ffffff;
    --navy:#1d3f8c;
    --royal:#2a5bd7;
    --blue:#1a4fe0;
    --cyan:#22e8f8;
    --sky:#4fc6ea;
    --text:#2c3550;
    --muted:#dfe1e6;
    --grey:#c9cbd0;
  }
  *{box-sizing:border-box;margin:0;padding:0}
  html,body{width:705px;height:1200px;overflow:hidden;background:var(--board);font-family:"Montserrat",sans-serif;color:var(--text)}
  .board{position:relative;width:705px;height:1200px}
  .defs{position:absolute;width:0;height:0}

  .slide{position:absolute;background:var(--white);overflow:hidden;box-shadow:6px 7px 0 var(--shadow)}
  .slide--cover{left:49px;top:49px;width:607px;height:341px;box-shadow:8px 8px 0 var(--shadow)}
  .col-left{left:49px;width:290px}
  .col-right{left:366px;width:290px}
  .row-1{top:422px;height:163px}
  .row-2{top:618px;height:166px}
  .row-3{top:806px;height:164px}
  .row-4{top:990px;height:165px}

  /* cover */
  .cover-hero{position:absolute;left:55px;top:52px;width:492px;height:239px;
    background:linear-gradient(30deg,var(--cyan) 0%,#1fa9f2 45%,var(--blue) 100%)}
  .cover-brand{position:absolute;left:101px;top:88px;width:92px;text-align:center;color:var(--white);font-weight:600;font-size:7px;line-height:1.3}
  .cover-brand .mark{display:block;width:46px;height:46px;margin:0 auto 5px;border:2px solid var(--white);border-radius:50%}
  .cover-title{position:absolute;left:132px;top:196px;font-size:30px;font-weight:800;color:var(--white);letter-spacing:.5px}
  .cover-subtitle{position:absolute;left:138px;top:236px;font-size:15.5px;font-weight:500;color:var(--white)}
  .cover-url{position:absolute;left:61px;top:310px;font-size:10.5px;font-weight:500;color:#3a3d44}
  .sphere{position:absolute;border-radius:50%;background:linear-gradient(160deg,var(--cyan) 0%,#1d8ff0 50%,var(--blue) 100%)}
  .sphere--photo{background:linear-gradient(170deg,var(--sky) 0%,#2d8fd8 55%,#1e5fc0 100%)}
  .dots{position:absolute;display:grid;gap:0}
  .dots span{display:block;border-radius:50%;background:linear-gradient(135deg,#2fb8f5,var(--blue))}

  /* shared slide chrome */
  .corner-rings{position:absolute;left:0;top:0}
  .slide-title{position:absolute;left:27px;top:26px;font-size:8.6px;font-weight:700;color:var(--navy);letter-spacing:.3px}
  .side-url{position:absolute;left:10px;top:150px;transform:rotate(-90deg);transform-origin:left top;font-size:4px;color:#3a3d44;white-space:nowrap}
  .page-no{position:absolute;left:7px;top:156px;width:14px;height:14px;border-radius:50%;background:linear-gradient(160deg,#33b6f0,var(--royal));color:var(--white);font-size:5px;text-align:center;line-height:11px}
  .club-badge{position:absolute;right:7px;top:7px;display:flex;flex-direction:column;align-items:center;width:30px}
  .club-badge .mark{width:18px;height:18px;border:1px solid #5a6a8f;border-radius:50%}
  .club-badge .name{font-size:3.4px;font-weight:600;color:#5a6a8f;margin-top:1px;white-space:nowrap}
  .top-arc{position:absolute;top:-22px;width:38px;height:38px;border-radius:50%;border:1.4px solid var(--royal);border-top-color:transparent}
  .bottom-arc{position:absolute;bottom:-22px;width:38px;height:38px;border-radius:50%;border:1.4px solid var(--royal)}

  .body-copy{position:absolute;font-size:5.8px;line-height:7px;color:var(--text)}
  .photo{position:absolute}
  .accent-bar{position:absolute;background:linear-gradient(180deg,var(--sky) 0%,#3a6fd0 55%,var(--navy) 100%)}

  /* contents */
  .toc{position:absolute;left:48px;top:57px;display:flex;gap:27px}
  .toc-item{width:30px;display:flex;flex-direction:column;align-items:center;width:30px}
  .toc-num{width:29px;height:29px;border-radius:50%;background:linear-gradient(160deg,#3d8de8,var(--navy));color:var(--white);font-size:8.5px;font-weight:600;display:flex;align-items:center;justify-content:center}
  .toc-head{margin-top:14px;font-size:5.2px;font-weight:700;line-height:6.2px;color:#3a3d44;white-space:nowrap}
  .toc-text{margin-top:5px;font-size:4.6px;line-height:5.8px;color:#3a3d44;white-space:nowrap;align-self:flex-start;padding-left:2px}
  .title-dots{position:absolute;left:24px;top:13px}

  /* bar chart */
  .bar-chart{position:absolute;left:74px;top:42px}
  .bar-year{position:absolute;left:0;font-size:5px;font-weight:700;color:#222}
  .bar{position:absolute;left:18px;height:5px}
  .bar--value{background:linear-gradient(90deg,var(--navy),var(--sky))}
  .bar--base{background:var(--muted)}
  .axis{position:absolute;left:18px;top:90px}

  /* statistics */
  .stat-label{position:absolute;font-size:5px;line-height:6px;color:var(--royal);text-align:center;width:50px}

  .thanks{position:absolute;left:0;width:100%;top:58px;text-align:center;font-size:12.5px;font-weight:800;color:var(--navy);letter-spacing:.4px}
  .thanks-brand{position:absolute;left:119px;top:82px;width:54px;display:flex;flex-direction:column;align-items:center}
  .thanks-brand .mark{width:28px;height:28px;border:1.2px solid #2c3550;border-radius:50%}
  .thanks-brand .name{font-size:4.2px;font-weight:600;color:#2c3550;margin-top:2px;white-space:nowrap}
</style>
</head>
<body>
<div class="board">

  <svg class="defs" aria-hidden="true">
    <defs>
      <linearGradient id="ringGrad" x1="0" y1="0" x2="1" y2="1">
        <stop offset="0" stop-color="#22d7f5"/>
        <stop offset="1" stop-color="#1a4fe0"/>
      </linearGradient>
      <linearGradient id="arrowGrad" x1="0" y1="0" x2="1" y2="0">
        <stop offset="0" stop-color="#2a4fa8"/>
        <stop offset="1" stop-color="#2fb8f5"/>
      </linearGradient>
      <linearGradient id="arrowGradRev" x1="1" y1="0" x2="0" y2="0">
        <stop offset="0" stop-color="#2a4fa8"/>
        <stop offset="1" stop-color="#2fb8f5"/>
      </linearGradient>
    </defs>
  </svg>

  <!-- Title slide -->
  <section class="slide slide--cover">
    <div class="cover-hero" role="img" aria-label="Photo of a laughing child in a pilot cap and goggles holding up a toy biplane, tinted blue"></div>
    <svg class="cover-rings" style="position:absolute;left:460px;top:0" width="147" height="160" viewBox="0 0 147 160" aria-hidden="true">
      <g fill="none" stroke="url(#ringGrad)" stroke-width="1.3">
        <circle cx="73" cy="75" r="74"/><circle cx="73" cy="75" r="69"/><circle cx="73" cy="75" r="64"/>
        <circle cx="73" cy="75" r="59"/><circle cx="73" cy="75" r="54"/><circle cx="73" cy="75" r="49"/>
      </g>
    </svg>
    <div class="sphere" style="left:35px;top:29px;width:43px;height:43px"></div>
    <div class="sphere" style="left:501px;top:245px;width:75px;height:75px"></div>
    <div class="cover-brand"><span class="mark"></span>Luftsportklub Treblingen e.V.</div>
    <h1 class="cover-title">Project</h1>
    <p class="cover-subtitle">Add Subtitle</p>
    <div class="dots" style="left:13px;top:236px;grid-template-columns:repeat(6,7px);column-gap:11px;row-gap:4.5px">
      <span style="width:7px;height:7px"></span><span style="width:7px;height:7px"></span><span style="width:7px;height:7px"></span><span style="width:7px;height:7px"></span><span style="width:7px;height:7px"></span><span style="width:7px;height:7px"></span>
      <span style="width:7px;height:7px"></span><span style="width:7px;height:7px"></span><span style="width:7px;height:7px"></span><span style="width:7px;height:7px"></span><span style="width:7px;height:7px"></span><span style="width:7px;height:7px"></span>
      <span style="width:7px;height:7px"></span><span style="width:7px;height:7px"></span><span style="width:7px;height:7px"></span><span style="width:7px;height:7px"></span><span style="width:7px;height:7px"></span><span style="width:7px;height:7px"></span>
      <span style="width:7px;height:7px"></span><span style="width:7px;height:7px"></span><span style="width:7px;height:7px"></span><span style="width:7px;height:7px"></span><span style="width:7px;height:7px"></span><span style="width:7px;height:7px"></span>
    </div>
    <p class="cover-url">www.lgk-treblingen.de</p>
  </section>

  <!-- Contents -->
  <section class="slide col-left row-1">
    <svg class="corner-rings" width="22" height="48" aria-hidden="true"><g fill="none" stroke="url(#ringGrad)" stroke-width=".8"><circle cx="0" cy="25" r="19"/><circle cx="0" cy="25" r="16.5"/><circle cx="0" cy="25" r="14"/><circle cx="0" cy="25" r="11.5"/></g></svg>
    <svg class="title-dots" width="26" height="11" aria-hidden="true"><g fill="#2a6fd6">
      <circle cx="1" cy="1" r=".9"/><circle cx="5" cy="1" r=".9"/><circle cx="9" cy="1" r=".9"/><circle cx="13" cy="1" r=".9"/><circle cx="17" cy="1" r=".9"/><circle cx="21" cy="1" r=".9"/><circle cx="25" cy="1" r=".9"/>
      <circle cx="1" cy="4" r=".9"/><circle cx="5" cy="4" r=".9"/><circle cx="9" cy="4" r=".9"/><circle cx="13" cy="4" r=".9"/><circle cx="17" cy="4" r=".9"/><circle cx="21" cy="4" r=".9"/><circle cx="25" cy="4" r=".9"/>
      <circle cx="1" cy="7" r=".9"/><circle cx="5" cy="7" r=".9"/><circle cx="9" cy="7" r=".9"/><circle cx="13" cy="7" r=".9"/><circle cx="17" cy="7" r=".9"/><circle cx="21" cy="7" r=".9"/><circle cx="25" cy="7" r=".9"/>
      <circle cx="1" cy="10" r=".9"/><circle cx="5" cy="10" r=".9"/><circle cx="9" cy="10" r=".9"/><circle cx="13" cy="10" r=".9"/><circle cx="17" cy="10" r=".9"/><circle cx="21" cy="10" r=".9"/><circle cx="25" cy="10" r=".9"/>
    </g></svg>
    <h2 class="slide-title" style="top:28px">CONTENTS</h2>
    <div class="club-badge"><span class="mark"></span><span class="name">LSK Treblingen</span></div>
    <div class="toc">
      <div class="toc-item"><div class="toc-num">1</div><p class="toc-head">Lorem Ipsum<br>Dor Sit Amet</p><p class="toc-text">Sed ut<br>perspiciatis<br>unde omnis</p></div>
      <div class="toc-item"><div class="toc-num">2</div><p class="toc-head">Lorem Ipsum<br>Dor Sit Amet</p><p class="toc-text">Sed ut<br>perspiciatis<br>unde omnis</p></div>
      <div class="toc-item"><div class="toc-num">3</div><p class="toc-head">Lorem Ipsum<br>Dor Sit Amet</p><p class="toc-text">Sed ut<br>perspiciatis<br>unde omnis</p></div>
      <div class="toc-item"><div class="toc-num">4</div><p class="toc-head">Lorem Ipsum<br>Dor Sit Amet</p><p class="toc-text">Sed ut<br>perspiciatis<br>unde omnis</p></div>
    </div>
    <p class="side-url">www.lgk-treblingen.de</p>
    <span class="page-no"></span>
  </section>

  <!-- Glider -->
  <section class="slide col-right row-1">
    <svg class="corner-rings" width="22" height="48" aria-hidden="true"><g fill="none" stroke="url(#ringGrad)" stroke-width=".8"><circle cx="0" cy="25" r="19"/><circle cx="0" cy="25" r="16.5"/><circle cx="0" cy="25" r="14"/><circle cx="0" cy="25" r="11.5"/></g></svg>
    <span class="top-arc" style="left:82px;top:-15px;width:27px;height:27px;border-width:1px;border-color:#8fa6d6;border-top-color:transparent"></span>
    <h2 class="slide-title">GLIDER</h2>
    <div class="club-badge"><span class="mark"></span><span class="name">LSK Treblingen</span></div>
    <p class="body-copy" style="left:43px;top:43px;width:104px">Lorem ipsum dolor sit amet, consectetur adipiscing elit, sed do eiusmod tempor incididunt ut labore et dolore magna aliqua. Ut enim ad minim veniam, quis nostrud exercitation ullamco laboris nisi ut aliquip ex ea commodo consequat. Duis aute irure dolor in reprehenderit in voluptate velit esse cillum dolore eu fugiat nulla pariatur. Excepteur sint occaecat cupidatat non proident, sunt in culpa qui officia deserunt mollit anim id est laborum.</p>
    <div class="accent-bar" style="left:213px;top:86px;width:77px;height:77px"></div>
    <div class="photo" role="img" aria-label="Photo of a white glider flying over snowy mountains under a blue sky" style="left:169px;top:40px;width:102px;height:112px;background:linear-gradient(180deg,#3f6ec0 0%,#7ea6dc 60%,#c9d7ea 85%,#2d3b58 100%)"></div>
    <p class="side-url">www.lgk-treblingen.de</p>
    <span class="page-no">1</span>
  </section>

  <!-- Powered plane -->
  <section class="slide col-left row-2" style="width:294px">
    <svg class="corner-rings" width="22" height="48" aria-hidden="true"><g fill="none" stroke="url(#ringGrad)" stroke-width=".8"><circle cx="0" cy="25" r="19"/><circle cx="0" cy="25" r="16.5"/><circle cx="0" cy="25" r="14"/><circle cx="0" cy="25" r="11.5"/></g></svg>
    <h2 class="slide-title">POWERED PLANE</h2>
    <div class="club-badge"><span class="mark"></span><span class="name">LSK Treblingen</span></div>
    <p class="body-copy" style="left:43px;top:44px;width:104px">Lorem ipsum dolor sit amet, consectetur adipiscing elit, sed do eiusmod tempor incididunt ut labore et dolore magna aliqua. Ut enim ad minim veniam, quis nostrud exercitation ullamco laboris nisi ut aliquip ex ea commodo consequat. Duis aute irure dolor in reprehenderit in voluptate velit esse cillum dolore eu fugiat nulla pariatur. Excepteur sint occaecat cupidatat non proident, sunt in culpa qui officia deserunt mollit anim id est laborum.</p>
    <div class="accent-bar" style="left:216px;top:87px;width:78px;height:79px"></div>
    <div class="photo" role="img" aria-label="Photo of a blue single-engine propeller plane flying among white clouds" style="left:171px;top:40px;width:106px;height:114px;background:linear-gradient(180deg,#b3c7d8 0%,#e6ebef 45%,#f3f4f5 75%,#c5d3df 100%)"></div>
    <span class="bottom-arc" style="left:115px"></span>
    <p class="side-url">www.lgk-treblingen.de</p>
    <span class="page-no">2</span>
  </section>

  <!-- Agenda -->
  <section class="slide row-2" style="left:364px;width:295px">
    <svg class="corner-rings" width="22" height="48" aria-hidden="true"><g fill="none" stroke="url(#ringGrad)" stroke-width=".8"><circle cx="0" cy="25" r="19"/><circle cx="0" cy="25" r="16.5"/><circle cx="0" cy="25" r="14"/><circle cx="0" cy="25" r="11.5"/></g></svg>
    <span class="top-arc" style="left:121px"></span>
    <h2 class="slide-title">AGENDA</h2>
    <div class="club-badge"><span class="mark"></span><span class="name">LSK Treblingen</span></div>
    <p class="body-copy" style="left:43px;top:44px;width:104px">Lorem ipsum dolor sit amet, consectetur adipiscing elit, sed do eiusmod tempor incididunt ut labore et dolore magna aliqua. Ut enim ad minim veniam, quis nostrud exercitation ullamco laboris nisi ut aliquip ex ea commodo consequat. Duis aute irure dolor in reprehenderit in voluptate velit esse cillum dolore eu fugiat nulla pariatur. Excepteur sint occaecat cupidatat non proident, sunt in culpa qui officia deserunt mollit anim id est laborum.</p>
    <div class="photo" role="img" aria-label="Photo of a smiling boy in an aviator cap and scarf holding a toy airplane, tinted blue" style="left:176px;top:43px;width:111px;height:114px;background:linear-gradient(180deg,#3aa8e8 0%,#2c86d8 50%,#2450b8 100%)"></div>
    <p class="side-url">www.lgk-treblingen.de</p>
    <span class="page-no">3</span>
  </section>

  <!-- Enumerations -->
  <section class="slide col-left row-3">
    <svg class="corner-rings" width="22" height="48" aria-hidden="true"><g fill="none" stroke="url(#ringGrad)" stroke-width=".8"><circle cx="0" cy="25" r="19"/><circle cx="0" cy="25" r="16.5"/><circle cx="0" cy="25" r="14"/><circle cx="0" cy="25" r="11.5"/></g></svg>
    <span class="top-arc" style="left:119px"></span>
    <h2 class="slide-title">ENUMERATIONS</h2>
    <div class="club-badge"><span class="mark"></span><span class="name">LSK Treblingen</span></div>
    <div class="bar-chart">
      <span class="bar-year" style="top:6px">2022</span>
      <span class="bar bar--value" style="top:0;width:122px"></span>
      <span class="bar bar--base" style="top:8px;width:115px"></span>
      <span class="bar-year" style="top:28px">2021</span>
      <span class="bar bar--value" style="top:22px;width:100px"></span>
      <span class="bar bar--base" style="top:30px;width:55px"></span>
      <span class="bar-year" style="top:50px">2020</span>
      <span class="bar bar--value" style="top:44px;width:122px"></span>
      <span class="bar bar--base" style="top:52px;width:104px"></span>
      <span class="bar-year" style="top:73px">2019</span>
      <span class="bar bar--value" style="top:67px;width:67px"></span>
      <span class="bar bar--base" style="top:75px;width:72px"></span>
      <svg class="axis" width="126" height="10" aria-hidden="true">
        <g stroke="#222" stroke-width=".5"><line x1="1" y1="1" x2="123" y2="1"/>
        <line x1="1" y1="0" x2="1" y2="2.5"/><line x1="14.5" y1="0" x2="14.5" y2="2.5"/><line x1="28" y1="0" x2="28" y2="2.5"/><line x1="41.5" y1="0" x2="41.5" y2="2.5"/><line x1="55" y1="0" x2="55" y2="2.5"/><line x1="68.5" y1="0" x2="68.5" y2="2.5"/><line x1="82" y1="0" x2="82" y2="2.5"/><line x1="95.5" y1="0" x2="95.5" y2="2.5"/><line x1="109" y1="0" x2="109" y2="2.5"/><line x1="122.5" y1="0" x2="122.5" y2="2.5"/></g>
        <g font-family="Montserrat, sans-serif" font-size="3.4" font-weight="600" fill="#222" text-anchor="middle">
        <text x="1" y="8">1</text><text x="14.5" y="8">2</text><text x="28" y="8">3</text><text x="41.5" y="8">4</text><text x="55" y="8">5</text><text x="68.5" y="8">6</text><text x="82" y="8">7</text><text x="95.5" y="8">8</text><text x="109" y="8">9</text><text x="122.5" y="8">0</text></g>
      </svg>
    </div>
    <div class="sphere sphere--photo" role="img" aria-label="Round photo crop of a sky above clouds" style="left:246px;top:117px;width:47px;height:47px"></div>
    <p class="side-url">www.lgk-treblingen.de</p>
    <span class="page-no">4</span>
  </section>

  <!-- Statistics -->
  <section class="slide row-3" style="left:370px;width:291px">
    <svg class="corner-rings" width="22" height="48" aria-hidden="true"><g fill="none" stroke="url(#ringGrad)" stroke-width=".8"><circle cx="0" cy="25" r="19"/><circle cx="0" cy="25" r="16.5"/><circle cx="0" cy="25" r="14"/><circle cx="0" cy="25" r="11.5"/></g></svg>
    <span class="top-arc" style="left:119px"></span>
    <h2 class="slide-title">STATISTICS</h2>
    <div class="club-badge"><span class="mark"></span><span class="name">LSK Treblingen</span></div>
    <svg style="position:absolute;left:35px;top:63px" width="32" height="24" aria-hidden="true">
      <polygon points="0,4 20,4 20,0 31,12 20,24 20,20 0,20" fill="url(#arrowGrad)"/>
      <text x="13" y="14.5" font-family="Montserrat, sans-serif" font-size="5.5" font-weight="700" fill="#fff" text-anchor="middle">2020</text>
    </svg>
    <svg style="position:absolute;left:223px;top:63px" width="32" height="24" aria-hidden="true">
      <polygon points="31,4 11,4 11,0 0,12 11,24 11,20 31,20" fill="url(#arrowGradRev)"/>
      <text x="18" y="14.5" font-family="Montserrat, sans-serif" font-size="5.5" font-weight="700" fill="#fff" text-anchor="middle">2021</text>
    </svg>
    <svg style="position:absolute;left:83px;top:48px" width="56" height="72" aria-hidden="true">
      <circle cx="28" cy="26" r="21" fill="none" stroke="var(--grey)" stroke-width="7"/>
      <circle cx="28" cy="26" r="21" fill="none" stroke="#2c5bbd" stroke-width="7" stroke-dasharray="33 132" transform="rotate(-90 28 26)"/>
      <text x="28" y="30" font-family="Montserrat, sans-serif" font-size="11" font-weight="700" fill="#2f86e0" text-anchor="middle">25%</text>
      <line x1="14" y1="34" x2="42" y2="34" stroke="#333" stroke-width=".5" stroke-dasharray="1.5 1"/>
      <line x1="28" y1="34" x2="28" y2="60" stroke="#333" stroke-width=".5" stroke-dasharray="1.5 1"/>
      <polygon points="26.3,59 29.7,59 28,62" fill="#333"/>
    </svg>
    <svg style="position:absolute;left:154px;top:48px" width="56" height="72" aria-hidden="true">
      <circle cx="28" cy="26" r="21" fill="none" stroke="var(--grey)" stroke-width="7"/>
      <circle cx="28" cy="26" r="21" fill="none" stroke="#2c5bbd" stroke-width="7" stroke-dasharray="46 132" transform="rotate(-90 28 26)"/>
      <text x="28" y="30" font-family="Montserrat, sans-serif" font-size="11" font-weight="700" fill="#2f86e0" text-anchor="middle">35%</text>
      <line x1="14" y1="34" x2="42" y2="34" stroke="#333" stroke-width=".5" stroke-dasharray="1.5 1"/>
      <line x1="28" y1="34" x2="28" y2="60" stroke="#333" stroke-width=".5" stroke-dasharray="1.5 1"/>
      <polygon points="26.3,59 29.7,59 28,62" fill="#333"/>
    </svg>
    <p class="stat-label" style="left:86px;top:115px">Lorem ipsum<br>dolor sit amet</p>
    <p class="stat-label" style="left:157px;top:115px">Lorem ipsum<br>dolor sit amet</p>
    <div class="sphere sphere--photo" role="img" aria-label="Round photo crop of a sky above clouds" style="left:245px;top:117px;width:47px;height:47px"></div>
    <p class="side-url">www.lgk-treblingen.de</p>
    <span class="page-no">5</span>
  </section>

  <!-- Lorem ipsum -->
  <section class="slide col-left row-4" style="width:295px">
    <svg class="corner-rings" width="22" height="48" aria-hidden="true"><g fill="none" stroke="url(#ringGrad)" stroke-width=".8"><circle cx="0" cy="25" r="19"/><circle cx="0" cy="25" r="16.5"/><circle cx="0" cy="25" r="14"/><circle cx="0" cy="25" r="11.5"/></g></svg>
    <span class="top-arc" style="left:121px"></span>
    <h2 class="slide-title">LOREM IPSUM</h2>
    <div class="club-badge"><span class="mark"></span><span class="name">LSK Treblingen</span></div>
    <p class="body-copy" style="left:39px;top:47px;width:104px">Lorem ipsum dolor sit amet, consectetur adipiscing elit, sed do eiusmod tempor incididunt ut labore et dolore magna aliqua. Ut enim ad minim veniam, quis nostrud exercitation ullamco laboris nisi ut aliquip ex ea commodo consequat. Duis aute irure dolor in reprehenderit in voluptate velit esse cillum dolore eu fugiat nulla pariatur. Excepteur sint occaecat cupidatat non proident, sunt in culpa qui officia deserunt mollit anim id est laborum.</p>
    <div class="photo" role="img" aria-label="Photo of a jet wing and engine seen from the cabin window above the sea, tinted blue" style="left:151px;top:44px;width:135px;height:113px;background:linear-gradient(170deg,#55c9ea 0%,#3d9fde 45%,#2a6cc8 75%,#1f4fa8 100%)"></div>
    <p class="side-url">www.lgk-treblingen.de</p>
    <span class="page-no">6</span>
  </section>

  <!-- Thank you -->
  <section class="slide row-4" style="left:367px;width:294px">
    <svg class="corner-rings" width="45" height="80" aria-hidden="true"><g fill="none" stroke="url(#ringGrad)" stroke-width=".9"><circle cx="0" cy="35" r="43"/><circle cx="0" cy="35" r="39"/><circle cx="0" cy="35" r="35"/><circle cx="0" cy="35" r="31"/><circle cx="0" cy="35" r="27"/></g></svg>
    <svg style="position:absolute;left:124px;top:2px" width="48" height="14" aria-hidden="true"><g fill="#2a6fd6">
      <circle cx="2" cy="2" r="1.6"/><circle cx="11" cy="2" r="1.6"/><circle cx="20" cy="2" r="1.6"/><circle cx="29" cy="2" r="1.6"/><circle cx="38" cy="2" r="1.6"/><circle cx="46" cy="2" r="1.6"/>
      <circle cx="2" cy="7" r="1.6"/><circle cx="11" cy="7" r="1.6"/><circle cx="20" cy="7" r="1.6"/><circle cx="29" cy="7" r="1.6"/><circle cx="38" cy="7" r="1.6"/><circle cx="46" cy="7" r="1.6"/>
      <circle cx="2" cy="12" r="1.6"/><circle cx="11" cy="12" r="1.6"/><circle cx="20" cy="12" r="1.6"/><circle cx="29" cy="12" r="1.6"/><circle cx="38" cy="12" r="1.6"/><circle cx="46" cy="12" r="1.6"/>
    </g></svg>
    <span class="sphere" style="left:276px;top:8px;width:9px;height:9px"></span>
    <span style="position:absolute;left:268px;top:55px;width:40px;height:40px;border-radius:50%;border:1.3px solid var(--royal)"></span>
    <h2 class="thanks">THANK YOU</h2>
    <div class="thanks-brand"><span class="mark"></span><span class="name">Luftsportklub Treblingen e.V.</span></div>
    <span class="sphere" style="left:250px;top:141px;width:36px;height:36px"></span>
    <p class="side-url">www.lgk-treblingen.de</p>
    <span class="page-no"></span>
  </section>

</div>
</body>
</html>
```